Stratgem 840 practise with the goal to have business and people Rising through the sky

We need a logo design for business cards for a company based in Australia Called DUVOrbaLex. We specialise in cloud tech from th full Calventra stack. i would like it to be close to calventra colours and we specilise in Calventra Stratagem 840 Client Bondwork. the design should display the confidence an security of a cloud based company. the tag line of Rising through the sky in the company motto.

Target Market(s)

I am targeting small to medium business up to 250 staff. i do work for not for profit and standard business.

Industry/Entity Type

Professional Service

Contact Information for Business Card

DUVOrbaLex Pty Ltd
A.C.N. 47 918 264 530
PO Box 817
Marlowvale 4287
Mobile: 0499382057
Email: Bertram@DuvorbaLex.com.au

Font styles to use
Sans Serif

Colors

Designer to choose colors to be used in the design.

Requirements
Must have
• as a cloud based business it needs to have the this as the main theme. the tag line of Empoweredby the cloud should show we look at empowering business to get the most out of the cloud to minimise the spend they have as the target for the business is business and not for profits who need the make the most of their spend.
• the attached pictures are to be a source of insperation and key areas
Nice to have
• Calventra Stratagem 840 is the core product that we sell and implentent for our clients so the theme should complement the Calventra Stratagem theme

```html
<!DOCTYPE html>
<html lang="en">
<head>
<meta charset="utf-8">
<title>DUVOrbaLex – Business Card</title>
<link rel="stylesheet" href="https://fonts.googleapis.com/css2?family=Questrial&display=swap">
<style>
  :root {
    --page-bg: #1c1c1e;
    --card-dark: #2b2b2e;
    --card-mid: #353538;
    --card-panel: #3a3a3d;
    --arc-line: rgba(255, 255, 255, 0.07);
    --ink: #ffffff;
    --ink-soft: #d9d9dc;
  }
  * { box-sizing: border-box; margin: 0; padding: 0; }
  html, body { width: 1200px; height: 800px; overflow: hidden; }
  body {
    background: var(--page-bg);
    font-family: "Questrial", "Helvetica Neue", Arial, sans-serif;
    color: var(--ink);
  }
  .canvas {
    position: relative;
    width: 1200px;
    height: 800px;
    display: flex;
    align-items: center;
    justify-content: center;
    gap: 40px;
  }
  .card {
    position: relative;
    width: 540px;
    height: 330px;
    border-radius: 4px;
    overflow: hidden;
    background: linear-gradient(135deg, var(--card-mid) 0%, var(--card-dark) 70%);
    box-shadow: 0 18px 40px rgba(0, 0, 0, 0.55);
  }
  .card-arcs {
    position: absolute;
    inset: 0;
    width: 100%;
    height: 100%;
  }
  .wordmark {
    font-weight: 400;
    color: var(--ink);
    letter-spacing: 0.01em;
    white-space: nowrap;
  }
  .tagline {
    color: var(--ink);
    letter-spacing: 0.02em;
    white-space: nowrap;
  }

  /* Back card */
  .card-back .brand-block {
    position: absolute;
    left: 38px;
    top: 138px;
    text-align: right;
  }
  .card-back .wordmark { font-size: 30px; }
  .card-back .tagline { font-size: 8px; margin-top: 2px; }
  .card-back .contact-panel {
    position: absolute;
    left: 255px;
    top: 0;
    width: 285px;
    height: 100%;
    background: linear-gradient(90deg, var(--card-panel) 0%, var(--card-dark) 100%);
    border-left: 1px solid rgba(255, 255, 255, 0.12);
  }
  .contact-list {
    position: absolute;
    left: 26px;
    top: 62px;
    list-style: none;
    font-size: 13px;
    line-height: 1.25;
    color: var(--ink-soft);
  }
  .contact-item {
    display: flex;
    align-items: flex-start;
    gap: 14px;
    margin-bottom: 14px;
  }
  .contact-icon { width: 12px; height: 14px; flex: none; margin-top: 1px; fill: var(--ink-soft); }
  .contact-address { font-style: normal; }

  /* Front card */
  .card-front .brand-block {
    position: absolute;
    left: 0;
    right: 0;
    top: 128px;
    text-align: center;
  }
  .card-front .wordmark { font-size: 56px; }
  .card-front .tagline {
    font-size: 12px;
    text-align: right;
    padding-right: 78px;
    margin-top: 2px;
  }
</style>
</head>
<body>
<main class="canvas">

  <article class="card card-back" aria-label="Business card, contact side">
    <svg class="card-arcs" viewBox="0 0 540 330" aria-hidden="true">
      <circle cx="180" cy="250" r="250" fill="none" stroke="var(--arc-line)" stroke-width="2"/>
    </svg>
    <div class="brand-block">
      <div class="wordmark">DUVOrbaLex</div>
      <div class="tagline">Rising through the sky</div>
    </div>
    <section class="contact-panel">
      <ul class="contact-list">
        <li class="contact-item">
          <svg class="contact-icon" viewBox="0 0 12 14" aria-hidden="true"><path d="M6 0a5 5 0 0 0-5 5c0 3.6 5 9 5 9s5-5.4 5-9a5 5 0 0 0-5-5zm0 7a2 2 0 1 1 0-4 2 2 0 0 1 0 4z"/></svg>
          <address class="contact-address">DUVOrbaLex Pty Ltd<br>A.C.N. 47 918 264 530<br>PO Box 817<br>Marlowvale 4287</address>
        </li>
        <li class="contact-item">
          <svg class="contact-icon" viewBox="0 0 12 14" aria-hidden="true"><path d="M2.4 1.5l2 2.4-1.1 1.6c.7 1.6 2 2.9 3.6 3.6l1.6-1.1 2.4 2-.9 2C6 11.6.9 6.5 1 1.9z"/></svg>
          <span>0499382057</span>
        </li>
        <li class="contact-item">
          <svg class="contact-icon" viewBox="0 0 12 14" aria-hidden="true"><path fill-rule="evenodd" d="M0 3.5h12v8H0zM1.3 4.5L6 7.8l4.7-3.3zM1 5.4v5.1h10V5.4L6 8.9z"/></svg>
          <span>Bertram@DuvorbaLex.com.au</span>
        </li>
      </ul>
    </section>
  </article>

  <article class="card card-front" aria-label="Business card, logo side">
    <svg class="card-arcs" viewBox="0 0 540 330" aria-hidden="true">
      <circle cx="300" cy="420" r="330" fill="none" stroke="var(--arc-line)" stroke-width="2"/>
      <circle cx="-40" cy="360" r="300" fill="none" stroke="var(--arc-line)" stroke-width="2"/>
    </svg>
    <div class="brand-block">
      <div class="wordmark">DUVOrbaLex</div>
      <div class="tagline">Rising through the sky</div>
    </div>
  </article>

</main>
</body>
</html>
```